Wine Label Image to go to print

I have a sketch/ idea- just need it brought to graphic design for my label company, should be very simple.. Wine Molecule diagram, - See attached

The wine label will be mostly white on white embossed with some black and white sketch lines around the embossment - with my wine logo name in one corner and the wine name and year in the other

```html
<!DOCTYPE html>
<html lang="en">
<head>
<meta charset="utf-8">
<title>Veltora Wine Label</title>
<link rel="stylesheet" href="https://fonts.googleapis.com/css2?family=Cinzel:wght@700&family=Jost:wght@300;400&display=swap">
<style>
  :root {
    --backdrop: #2a2a2b;
    --label-paper: #f1f1f0;
    --ink: #161616;
    --wine-red: #8e0f17;
    --emboss-tone: #e4e4e3;
    --emboss-shade: #d2d2d1;
  }
  html, body {
    margin: 0;
    padding: 0;
    width: 1200px;
    height: 1200px;
    overflow: hidden;
    background: var(--backdrop);
  }
  .canvas {
    width: 1200px;
    height: 1200px;
    display: flex;
    align-items: center;
    justify-content: center;
  }
  .wine-label {
    position: relative;
    width: 720px;
    height: 860px;
    background: var(--label-paper);
    box-sizing: border-box;
  }
  .brand {
    position: absolute;
    top: 92px;
    left: 0;
    right: 0;
    display: flex;
    align-items: center;
    justify-content: center;
    gap: 20px;
  }
  .brand-name {
    margin: 0;
    font-family: "Cinzel", serif;
    font-weight: 700;
    font-size: 72px;
    line-height: 1;
    letter-spacing: 3px;
    color: var(--ink);
  }
  .brand-dot {
    width: 18px;
    height: 18px;
    border-radius: 50%;
    background: var(--wine-red);
    flex: none;
  }
  .molecule-emboss {
    position: absolute;
    top: 240px;
    left: 100px;
    width: 520px;
    height: 260px;
    background: radial-gradient(ellipse at center, var(--emboss-shade) 0%, var(--emboss-tone) 55%, var(--label-paper) 100%);
    border-radius: 8px;
  }
  .wine-name {
    position: absolute;
    top: 555px;
    left: 0;
    right: 0;
    text-align: center;
    margin: 0;
    font-family: "Jost", sans-serif;
    font-weight: 300;
    font-size: 50px;
    line-height: 1;
    letter-spacing: 13px;
    color: var(--ink);
  }
  .vintage {
    position: absolute;
    top: 690px;
    left: 150px;
    margin: 0;
    font-family: "Jost", sans-serif;
    font-weight: 400;
    font-size: 28px;
    line-height: 1;
    letter-spacing: 5px;
    color: var(--ink);
  }
</style>
</head>
<body>
  <main class="canvas">
    <section class="wine-label">
      <div class="brand">
        <h1 class="brand-name">VELTORA</h1>
        <span class="brand-dot" aria-hidden="true"></span>
      </div>
      <div class="molecule-emboss" role="img" aria-label="White-on-white embossed molecule diagram with fine black sketch lines"></div>
      <h2 class="wine-name">WINE NAME</h2>
      <p class="vintage">2024</p>
    </section>
  </main>
</body>
</html>
```